Maple Hollow Bloom Panels Business card

Looking to have a business card design incorporating my logo for my flower wall business.

Industry/Entity Type

Wedding & event planning

Contact Information for Business Card

My business logo, my name - Lena Whitcombe (owner), my tagline - Let us be your something extra, phone # 401-726-3148, email address - maplehollowbloompanels@mailvane.net, my website - maplehollowbloompanels.net, Instagram handle- @maplehollowbloompanels, FB handle Handle - maplehollowbloompanels

Font styles to use
Other font styles liked:
• Sentaina is the font that is used in my logo

Requirements
Must have
• Would like a double sided business card

```html
<!DOCTYPE html>
<html lang="en">
<head>
<meta charset="utf-8">
<title>Maple Hollow Bloom Panels – Business Card</title>
<link rel="stylesheet" href="https://fonts.googleapis.com/css2?family=Poppins:wght@400;500;600&family=Great+Vibes&display=swap">
<style>
  :root {
    --stage: #e8e6e7;
    --card-dark: #2a292b;
    --card-light: #ffffff;
    --ink: #141414;
    --silver: #d9d9dc;
    --pink: #e48fc0;
    --pink-soft: #f6dcea;
    --gold: #c9992c;
    --gold-light: #e6bf4e;
    --green: #34473a;
    --icon: #d66fa9;
  }
  * { margin: 0; padding: 0; box-sizing: border-box; }
  html, body { width: 1200px; height: 960px; overflow: hidden; }
  body {
    background: var(--stage);
    font-family: "Poppins", sans-serif;
    position: relative;
  }
  .card {
    position: absolute;
    left: 250px;
    width: 700px;
    height: 400px;
    border-radius: 26px;
    overflow: hidden;
    box-shadow: 0 14px 34px rgba(0,0,0,0.18);
  }
  /* Back side */
  .card-back { top: 50px; background: var(--card-dark); }
  .brand-mark {
    position: absolute;
    display: flex;
    align-items: center;
    gap: 12px;
  }
  .brand-dot {
    width: 14px; height: 14px; border-radius: 50%;
    background: var(--gold);
    flex: none;
  }
  .brand-name {
    font-family: "Poppins", sans-serif;
    font-weight: 500;
    letter-spacing: 0.04em;
    line-height: 1.25;
  }
  .card-back .brand-mark { left: 0; right: 0; top: 120px; justify-content: center; }
  .card-back .brand-name { color: var(--silver); font-size: 30px; text-align: center; }
  .tagline {
    position: absolute;
    left: 0; right: 0; top: 250px;
    text-align: center;
    font-family: "Great Vibes", cursive;
    font-size: 46px;
    color: var(--silver);
  }
  /* Front side */
  .card-front { top: 510px; background: var(--card-light); }
  .bloom-backdrop {
    position: absolute;
    right: -40px; top: -30px;
    width: 380px; height: 360px;
    border-radius: 50%;
    background: radial-gradient(circle at 50% 50%, var(--pink-soft) 0%, rgba(246,220,234,0.55) 55%, rgba(246,220,234,0) 72%);
  }
  .card-front .brand-mark { left: 40px; top: 150px; width: 230px; }
  .card-front .brand-name { color: var(--ink); font-size: 22px; }
  .contact-block { position: absolute; left: 310px; top: 88px; }
  .person-name {
    font-weight: 600;
    font-size: 28px;
    letter-spacing: 0.02em;
    text-transform: uppercase;
    color: var(--ink);
    line-height: 1.1;
  }
  .person-role { color: var(--pink); font-size: 17px; margin-bottom: 14px; }
  .contact-list { list-style: none; }
  .contact-list li {
    display: flex; align-items: center; gap: 10px;
    font-size: 15px; color: #2c2c2c; line-height: 27px;
  }
  .contact-list svg { width: 14px; height: 14px; flex: none; }
  .color-bands {
    position: absolute; left: 0; right: 0; bottom: 0; height: 13px;
    display: flex; gap: 6px;
  }
  .band { height: 100%; }
  .band-pink { flex: 36; background: var(--pink); }
  .band-gold { flex: 34; background: linear-gradient(90deg, var(--gold), var(--gold-light)); }
  .band-green { flex: 30; background: var(--green); }
</style>
</head>
<body>
  <section class="card card-back" aria-label="Card back">
    <div class="brand-mark">
      <span class="brand-dot"></span>
      <span class="brand-name">Maple Hollow<br>Bloom Panels</span>
    </div>
    <p class="tagline">Let us be your something extra</p>
  </section>

  <section class="card card-front" aria-label="Card front">
    <div class="bloom-backdrop" role="img" aria-label="Faint pink outline flower decoration"></div>
    <div class="brand-mark">
      <span class="brand-dot"></span>
      <span class="brand-name">Maple Hollow<br>Bloom Panels</span>
    </div>
    <div class="contact-block">
      <h1 class="person-name">Lena Whitcombe</h1>
      <p class="person-role">owner</p>
      <ul class="contact-list">
        <li>
          <svg viewBox="0 0 16 16" aria-hidden="true"><path fill="var(--icon)" d="M3.6 1.5l2.3-.4 1.3 3.2-1.6 1.2a8 8 0 0 0 4.9 4.9l1.2-1.6 3.2 1.3-.4 2.3c-.2.9-1 1.5-1.9 1.4A12.5 12.5 0 0 1 2.2 3.4c-.1-.9.5-1.7 1.4-1.9z"/></svg>
          401-726-3148
        </li>
        <li>
          <svg viewBox="0 0 16 16" aria-hidden="true"><rect x="1" y="3" width="14" height="10" rx="1.5" fill="var(--icon)"/><path d="M1.5 4l6.5 5 6.5-5" fill="none" stroke="#fff" stroke-width="1.4"/></svg>
          maplehollowbloompanels@mailvane.net
        </li>
        <li>
          <svg viewBox="0 0 16 16" aria-hidden="true"><circle cx="8" cy="8" r="6.5" fill="none" stroke="var(--icon)" stroke-width="1.6"/><ellipse cx="8" cy="8" rx="2.8" ry="6.5" fill="none" stroke="var(--icon)" stroke-width="1.3"/><path d="M1.5 8h13" stroke="var(--icon)" stroke-width="1.3"/></svg>
          maplehollowbloompanels.net
        </li>
        <li>
          <svg viewBox="0 0 16 16" aria-hidden="true"><circle cx="8" cy="8" r="7" fill="var(--icon)"/></svg>
          @maplehollowbloompanels
        </li>
        <li>
          <svg viewBox="0 0 16 16" aria-hidden="true"><circle cx="8" cy="8" r="7" fill="var(--icon)"/></svg>
          maplehollowbloompanels
        </li>
      </ul>
    </div>
    <div class="color-bands" aria-hidden="true">
      <span class="band band-pink"></span>
      <span class="band band-gold"></span>
      <span class="band band-green"></span>
    </div>
  </section>
</body>
</html>
```